Bright Path Safety billboard design project.

Bright Path Safety Ltd. is based in Quesnel BC and provides a variety of safety services including COR external auditing, safety training, over 500 online safety courses, mobile equipment training and heavy duty equipment training. We are looking for a billboard design with more of a focus on the mobile equipment training.

Target Market(s)

Construction, forestry and mining companies.

Colors
3276b5

Requirements
Must have
• Company Logo
website www.brightpathsafety-example.com

```html
<!DOCTYPE html>
<html lang="en">
<head>
<meta charset="utf-8">
<title>Bright Path Safety Ltd. – Billboard</title>
<link href="https://fonts.googleapis.com/css2?family=Chewy&display=swap" rel="stylesheet">
<style>
  :root {
    --sky-blue: #2ea3dc;
    --deep-blue: #1678b8;
    --pale-blue: #5fc3ee;
    --ink: #111111;
    --paper: #f3f7f9;
    --white: #ffffff;
    --rim-grey: #c9cdd0;
    --brand-navy: #0d1b2a;
  }
  * { box-sizing: border-box; margin: 0; padding: 0; }
  html, body {
    width: 1200px;
    height: 801px;
    overflow: hidden;
    background: var(--paper);
  }
  .billboard {
    position: relative;
    width: 1200px;
    height: 801px;
    overflow: hidden;
    background: linear-gradient(180deg, #fbfdfe 0%, var(--paper) 100%);
    font-family: "Chewy", "Arial Rounded MT Bold", sans-serif;
    font-weight: 400;
  }
  .intro {
    position: absolute;
    left: 56px;
    top: 52px;
    font-size: 40px;
    white-space: nowrap;
    color: var(--sky-blue);
    text-shadow: 2px 2px 0 #1c3550;
    letter-spacing: 0.5px;
  }
  .ribbon {
    position: absolute;
    left: 30px;
    top: 130px;
    width: 760px;
    height: 320px;
  }
  .ribbon-text {
    position: absolute;
    left: 70px;
    top: 196px;
    font-size: 48px;
    line-height: 1.25;
    white-space: nowrap;
    color: var(--ink);
    text-shadow: 2px 2px 0 rgba(255,255,255,0.55);
  }
  .services {
    position: absolute;
    left: 90px;
    top: 472px;
    width: 560px;
    text-align: center;
    list-style: none;
    font-size: 34px;
    line-height: 1.35;
    white-space: nowrap;
    color: var(--ink);
    text-shadow:
      -2px -2px 0 var(--white), 2px -2px 0 var(--white),
      -2px 2px 0 var(--white), 2px 2px 0 var(--white),
      3px 4px 3px rgba(0,0,0,0.35);
  }
  .brand-disc {
    position: absolute;
    left: 790px;
    top: 200px;
    width: 370px;
    height: 370px;
    border-radius: 50%;
    background: var(--white);
    box-shadow: -10px 8px 0 var(--rim-grey), -12px 12px 18px rgba(0,0,0,0.18);
    display: flex;
    align-items: center;
    justify-content: center;
    text-align: center;
  }
  .brand-name {
    font-size: 46px;
    line-height: 1.1;
    color: var(--brand-navy);
    padding: 0 50px;
  }
  .web-band {
    position: absolute;
    left: 620px;
    top: 640px;
    width: 580px;
    height: 100px;
    background: linear-gradient(90deg, rgba(46,163,220,0) 0%, var(--sky-blue) 28%, var(--deep-blue) 100%);
    display: flex;
    align-items: center;
    justify-content: flex-end;
    padding-right: 28px;
  }
  .web-address {
    font-size: 32px;
    white-space: nowrap;
    color: var(--white);
    letter-spacing: 0.5px;
  }
</style>
</head>
<body>
<main class="billboard">
  <p class="intro">We provides a variety of safety services</p>

  <svg class="ribbon" viewBox="0 0 820 300" preserveAspectRatio="none" aria-hidden="true">
    <defs>
      <linearGradient id="ribbonFill" x1="0" y1="0" x2="1" y2="0">
        <stop offset="0" stop-color="#2b9ad6"/>
        <stop offset="1" stop-color="#5fc3ee"/>
      </linearGradient>
    </defs>
    <path d="M20 18 C 120 0, 240 10, 330 40 L 330 60 C 240 40, 130 36, 20 46 Z" fill="#1678b8"/>
    <path d="M20 46 C 260 20, 440 130, 640 170 C 700 182, 760 186, 800 180
             L 760 230 L 820 298 C 740 300, 640 290, 560 270
             C 380 228, 220 150, 10 170 Z" fill="url(#ribbonFill)"/>
  </svg>
  <p class="ribbon-text">Mobile equipment training and<br>heavy duty equipment training.</p>

  <ul class="services">
    <li>Including COR external auditing</li>
    <li>Safety Training</li>
    <li>Over 500 online safety courses</li>
  </ul>

  <div class="brand-disc">
    <p class="brand-name">Bright Path Safety Ltd.</p>
  </div>

  <div class="web-band">
    <p class="web-address">www.brightpathsafety-example.com</p>
  </div>
</main>
</body>
</html>
```